Business card design needed

We do excavation, cartage and contracting
I would quote like to have a picture of my digger as the whole back ground and the words on top. If that looks any good
Otherwise please feel free to come up with any other cool options

Cheers Marc

KLR Contracting
Excavation, Cartage, Contracting
Marcus Prewitt
www.klr-example.co.nz
021 584 067
marc@klr-example.co.nz

```html
<!DOCTYPE html>
<html lang="en">
<head>
<meta charset="utf-8">
<title>KLR Contracting – Business Card</title>
<link rel="stylesheet" href="https://fonts.googleapis.com/css2?family=Cinzel:wght@400;600&family=Lato:wght@400;700&display=swap">
<style>
  :root {
    --backdrop: #2b2b2b;
    --green-deep: #0d5a22;
    --green-bright: #0a9a3e;
    --green-band: #1f5a1e;
    --yellow-panel: #d8c42a;
    --yellow-light: #e6d640;
    --ink-green: #1d4a1a;
    --white: #ffffff;
  }
  * { margin: 0; padding: 0; box-sizing: border-box; }
  html, body {
    width: 1200px;
    height: 900px;
    overflow: hidden;
    background: var(--backdrop);
  }
  .canvas {
    position: relative;
    width: 1200px;
    height: 900px;
  }
  .card {
    position: absolute;
    left: 250px;
    width: 700px;
    height: 400px;
    border-radius: 28px;
    overflow: hidden;
    box-shadow: 0 14px 34px rgba(0,0,0,.55);
  }

  /* Back side */
  .card-back {
    top: 40px;
    background: linear-gradient(160deg, var(--green-bright) 0%, #07833a 45%, var(--green-deep) 100%);
    display: flex;
    align-items: center;
    justify-content: center;
  }
  .back-brand {
    display: flex;
    align-items: center;
    gap: 22px;
    color: var(--white);
    font-family: "Cinzel", serif;
    font-weight: 400;
    font-size: 52px;
    letter-spacing: 4px;
  }
  .brand-square {
    width: 34px;
    height: 34px;
    border: 3px solid currentColor;
  }

  /* Front side */
  .card-front { top: 470px; }
  .site-photo {
    position: absolute;
    inset: 0;
    background:
      linear-gradient(180deg, #b9cde0 0%, #9fb7c9 9%, transparent 12%),
      linear-gradient(100deg, #4f8a2c 0%, #6aa236 28%, #8a7c4a 52%, #8b6c4c 72%, #7a5e42 100%);
  }
  .contact-panel {
    position: absolute;
    left: 290px;
    top: 165px;
    width: 410px;
    height: 235px;
    border-top-left-radius: 30px;
    background: linear-gradient(160deg, var(--yellow-light), var(--yellow-panel));
  }
  .panel-brand {
    position: absolute;
    left: 24px;
    top: 138px;
    display: flex;
    align-items: center;
    gap: 10px;
    color: var(--ink-green);
    font-family: "Cinzel", serif;
    font-weight: 600;
    font-size: 20px;
    letter-spacing: 1px;
    white-space: nowrap;
  }
  .panel-brand .brand-square { width: 18px; height: 18px; border-width: 2px; }
  .contact-block {
    position: absolute;
    left: 200px;
    top: 24px;
    color: var(--ink-green);
    font-family: "Lato", sans-serif;
  }
  .contact-name {
    font-size: 17px;
    letter-spacing: 1px;
    text-transform: uppercase;
    margin-bottom: 10px;
  }
  .contact-list { list-style: none; font-size: 12.5px; line-height: 19px; }
  .contact-list li { display: flex; gap: 14px; white-space: nowrap; }
  .contact-label { width: 10px; }
  .service-band {
    position: absolute;
    left: 0;
    bottom: 0;
    width: 100%;
    height: 48px;
    background: var(--green-band);
    color: var(--yellow-light);
    font-family: "Cinzel", serif;
    font-size: 15px;
    letter-spacing: 1px;
    white-space: nowrap;
    display: flex;
    align-items: center;
    justify-content: center;
  }
</style>
</head>
<body>
<main class="canvas">
  <section class="card card-back" aria-label="Card back">
    <div class="back-brand"><span class="brand-square"></span>KLR Contracting</div>
  </section>

  <section class="card card-front" aria-label="Card front">
    <div class="site-photo" role="img" aria-label="Photo of a yellow excavator on a dirt site with bush and river behind"></div>
    <div class="contact-panel">
      <div class="contact-block">
        <p class="contact-name">Marcus Prewitt</p>
        <ul class="contact-list">
          <li><span class="contact-label">P</span>021 584 067</li>
          <li><span class="contact-label">E</span>marc@klr-example.co.nz</li>
          <li><span class="contact-label">W</span>www.klr-example.co.nz</li>
        </ul>
      </div>
      <div class="panel-brand"><span class="brand-square"></span>KLR Contracting</div>
      <div class="service-band">EXCAVATION • CARTAGE • CONTRACTING</div>
    </div>
  </section>
</main>
</body>
</html>
```